High-End audio shop owner needs a business card

I need a personal Business Card for my Audio shop which exists since 1962. We offer high Quality brands, professional Attention and run our own repair-service-department. I look for a design which will be printed on high Quality paper and shall convey trust to the Client that we are very serious. Language is german.

```html
<!DOCTYPE html>
<html lang="de">
<head>
<meta charset="utf-8">
<title>Hi-Fi Lindenhof – Visitenkarte</title>
<link rel="stylesheet" href="https://fonts.googleapis.com/css2?family=Roboto:wght@400;500;700;900&display=swap">
<style>
  :root {
    --backdrop: #3a3a3a;
    --card: #1c1c1e;
    --card-edge: #0f0f10;
    --accent: #ff6a13;
    --emboss: #4a4a4d;
    --text-muted: #b9b9bb;
  }
  * { margin: 0; padding: 0; box-sizing: border-box; }
  html, body {
    width: 799px;
    height: 1200px;
    overflow: hidden;
  }
  body {
    background: var(--backdrop);
    font-family: "Roboto", sans-serif;
    display: flex;
    flex-direction: column;
    align-items: center;
    justify-content: space-around;
    padding: 60px 0;
  }
  .card {
    position: relative;
    width: 640px;
    height: 366px;
    background: var(--card);
    border: 1px solid var(--card-edge);
    box-shadow: 0 18px 40px rgba(0,0,0,0.45);
  }

  /* Front side */
  .card--front {
    display: flex;
    align-items: center;
    justify-content: center;
  }
  .front-brand {
    font-weight: 900;
    font-size: 44px;
    letter-spacing: 2px;
    text-transform: uppercase;
    color: var(--emboss);
  }

  /* Back side */
  .back-brand {
    position: absolute;
    left: 40px;
    top: 40px;
    font-weight: 900;
    font-size: 40px;
    letter-spacing: 1px;
    text-transform: uppercase;
    color: var(--accent);
  }
  .holder {
    position: absolute;
    left: 40px;
    top: 196px;
  }
  .holder-name {
    font-weight: 700;
    font-size: 19px;
    color: var(--accent);
  }
  .holder-role {
    margin-top: 4px;
    font-size: 14px;
    color: var(--text-muted);
  }
  .contact {
    position: absolute;
    right: 44px;
    bottom: 36px;
    font-size: 15px;
    line-height: 1.45;
    color: var(--text-muted);
  }
  .contact-address { margin-bottom: 6px; }
  .contact-line {
    display: flex;
    align-items: center;
    gap: 12px;
  }
  .contact-icon {
    width: 14px;
    height: 14px;
    fill: var(--accent);
    flex: none;
  }
</style>
</head>
<body>

  <section class="card card--front" aria-label="Vorderseite">
    <div class="front-brand">Hi-Fi Lindenhof</div>
  </section>

  <section class="card card--back" aria-label="Rückseite">
    <div class="back-brand">Hi-Fi Lindenhof</div>

    <div class="holder">
      <div class="holder-name">Martin Lindenhof</div>
      <div class="holder-role">Managing Director</div>
    </div>

    <div class="contact">
      <div class="contact-address">
        Seefeldgasse 18<br>
        CH-6005 Luzern
      </div>
      <div class="contact-line">
        <svg class="contact-icon" viewBox="0 0 24 24" aria-hidden="true">
          <path d="M6.6 10.8a15.1 15.1 0 0 0 6.6 6.6l2.2-2.2c.3-.3.7-.4 1-.2 1.1.4 2.3.6 3.6.6.6 0 1 .4 1 1V20c0 .6-.4 1-1 1A17 17 0 0 1 3 4c0-.6.4-1 1-1h3.5c.6 0 1 .4 1 1 0 1.3.2 2.5.6 3.6.1.3 0 .7-.2 1z"/>
        </svg>
        <span>041 555 01 47</span>
      </div>
      <div class="contact-line">
        <svg class="contact-icon" viewBox="0 0 24 24" aria-hidden="true">
          <path d="M2 5h20v14H2z M3.5 6.5 12 13l8.5-6.5" fill="var(--accent)"/>
          <path d="M3 6l9 7 9-7" fill="none" stroke="#1c1c1e" stroke-width="1.6"/>
        </svg>
        <span>info@hifi-lh.ch</span>
      </div>
      <div class="contact-line">
        <svg class="contact-icon" viewBox="0 0 24 24" aria-hidden="true">
          <circle cx="12" cy="12" r="10"/>
          <path d="M2 12h20M12 2c3 3 3 17 0 20M12 2c-3 3-3 17 0 20" fill="none" stroke="#1c1c1e" stroke-width="1.4"/>
        </svg>
        <span>www.hifi-lh.ch</span>
      </div>
    </div>
  </section>

</body>
</html>
```